Not another boring Business Card Design Project

This is not another boring Business Card Design Project.

We are looking for the weirdest, wackiest most boundary pushing designs that you can come up with.

If you believe that design can be fun, energetic, crazy, unpredictable, beautiful and eye-catching then read on… this project is for you.

We are Tolvin Presk and we print plastic cards.

We are running a Plastic Card Design Competition.

And we need a plastic card to advertise the competition to graphic designers just like you.

The design needs to make your average designers’ jaws drop and their eyes pop out.

You can do what you wish with the card design, so long as it stands out.

We like these designs, designs that stretch the boundaries and become something beyond just another business card:

http://quorvamedia.net/wp-content/uploads/2009/03/b48.jpg
Designer - http://www.pelvanworks.com/

http://quorvamedia.net/wp-content/uploads/2009/03/b41.jpg
Designer - http://renolbrakstad.com/

http://images.plinthhive.com/designs/44195_732292_37774_thumbnail.jpg
Designer- Zentro Media at Plinth Hive

http://images.plinthhive.com/designs/44195_717529_37774_thumbnail.jpg
Designer - Zentro Media at Plinth Hive

http://quorvamedia.net/wp-content/uploads/2009/03/b11.jpg
Designer - http://www.wk7studio.com/

http://quorvamedia.net/wp-content/uploads/2009/03/b16.jpg
Designer - http://www.pebbletumbler.com/

Reason: A number of designers have said they want to submit designs and haven't yet done so, we want to give them time.

Reason: We've extended the deadline by 4 days for those who want to submit their designs over the weekend and give ourselves time to judge them

Plastic

• The design needs to contain this link: lnk.example/QzRpLk and any other detail that will encourage competition entry. The design will be printed on plastic.
• No borders (when plastic cards are punched to shape and size there is movement of 1 - 2mm, borders highlight this movement).

Keep text 3mm away from edges of the cards.

Please don't create designs to be produced on clear/transparent plastic.

```html
<!DOCTYPE html>
<html lang="en">
<head>
<meta charset="utf-8">
<title>Plastic Card Design Competition – Card</title>
<link rel="stylesheet" href="https://fonts.googleapis.com/css2?family=Quicksand:wght@400;500&display=swap">
<style>
  :root {
    --bg-dark: #6c871d;
    --bg-mid: #86a122;
    --bg-light: #a4c12c;
    --card: #ffffff;
    --ink: #161616;
    --shadow: rgba(30, 45, 0, 0.45);
  }
  html, body {
    margin: 0;
    padding: 0;
    width: 1200px;
    height: 907px;
    overflow: hidden;
  }
  .stage {
    position: relative;
    width: 1200px;
    height: 907px;
    background: linear-gradient(135deg, var(--bg-dark) 0%, var(--bg-mid) 50%, var(--bg-light) 100%);
  }
  .card {
    position: absolute;
    left: 319px;
    width: 568px;
    height: 347px;
    border-radius: 34px;
    background: var(--card);
    box-shadow: 4px 5px 8px var(--shadow);
    overflow: hidden;
  }
  .card--front {
    top: 90px;
    display: flex;
    align-items: center;
    justify-content: center;
  }
  .card--back {
    top: 473px;
  }
  .outline-type {
    font-family: "Quicksand", sans-serif;
    font-weight: 500;
    color: transparent;
    -webkit-text-stroke: 1.6px var(--ink);
  }
  .card__link {
    margin: 0;
    font-size: 54px;
    letter-spacing: 0;
    transform: translateY(8px);
    white-space: nowrap;
  }
  .alphabet {
    position: absolute;
    left: 50%;
    top: 50%;
    margin: 0;
    display: flex;
    flex-direction: column;
    align-items: center;
    transform: translate(-50%, -50%) rotate(-48deg);
  }
  .alphabet__row {
    font-size: 118px;
    line-height: 150px;
    letter-spacing: 2px;
    white-space: nowrap;
  }
  .alphabet__row--1 { transform: translateX(-60px); }
  .alphabet__row--2 { transform: translateX(-20px); }
  .alphabet__row--3 { transform: translateX(10px); }
  .alphabet__row--4 { transform: translateX(40px); }
</style>
</head>
<body>
  <main class="stage">
    <section class="card card--front">
      <p class="card__link outline-type">lnk.example/QzRpLk</p>
    </section>
    <section class="card card--back">
      <div class="alphabet outline-type" aria-label="Lowercase alphabet">
        <span class="alphabet__row alphabet__row--1">abcdef</span>
        <span class="alphabet__row alphabet__row--2">ghijklm</span>
        <span class="alphabet__row alphabet__row--3">nopqrst</span>
        <span class="alphabet__row alphabet__row--4">uvwxyz</span>
      </div>
    </section>
  </main>
</body>
</html>
```